Word Bureau Ostrelle Templates

We run a large number of businesses, including schools, airports, hotels and offices. We write reports on a daily basis and are looking for a strong and sexy WORD Template. We already have a logo in place (see graphical chart attached), that is rights' protected. We are looking for a beautiful wich reflect modern design and human aspects. Our logo has 2 design, full fill and watermark. It can be used in red or black.

Architects, Fire brigade, Building investors, contactors

• Arial, Calibri, ...

• Cover page, summary, Bullet points, Tables, Figures, Annex

```html
<!DOCTYPE html>
<html lang="en">
<head>
<meta charset="utf-8">
<title>Bureau Ostrelle – Word Templates</title>
<link href="https://fonts.googleapis.com/css2?family=Arimo:ital,wght@0,400;0,700;1,400;1,700&family=Nunito+Sans:wght@400;700;800&display=swap" rel="stylesheet">
<style>
:root{
  --canvas:#e3e3e3;
  --paper:#ffffff;
  --paper-grey:#ececec;
  --red:#e8403a;
  --red-deep:#c9202a;
  --red-dark:#8e1a1f;
  --photo-red-a:#7a1416;
  --photo-red-b:#3a0708;
  --ink:#222222;
  --ink-soft:#555555;
  --cell-light:#e6e6e6;
  --cell-mid:#d3d3d3;
  --cell-dark:#bdbdbd;
}
*{margin:0;padding:0;box-sizing:border-box}
html,body{width:1200px;height:2419px;overflow:hidden;background:var(--canvas)}
body{position:relative;font-family:"Arimo",Arial,sans-serif;color:var(--ink)}
.page{position:absolute;width:506px;height:710px;overflow:hidden;background:var(--paper-grey);box-shadow:0 2px 6px rgba(0,0,0,.35)}
.page--white{background:var(--paper)}
.page svg.backdrop{position:absolute;left:0;top:0;width:506px;height:710px}
.abs{position:absolute}

.brand{position:absolute;display:flex;align-items:center;gap:8px;font-family:"Nunito Sans",sans-serif;font-weight:400;color:var(--ink);line-height:1}
.brand-dot{border-radius:50%;background:var(--red);flex:none}
.brand-name{display:block}

.section-title{position:absolute;font-family:"Arimo",Arial,sans-serif;font-weight:700;font-size:19px;color:var(--ink);white-space:nowrap}
.rule{position:absolute;height:2px;background:var(--red)}

.badge{position:absolute;width:30px;height:30px;border-radius:50%;background:#f5f5f5;border:2px solid var(--red-dark);box-shadow:0 1px 3px rgba(0,0,0,.45);display:flex;align-items:center;justify-content:center;font-weight:700;font-size:11px;color:var(--ink)}
.item h4{font-size:11px;font-weight:700;color:var(--ink);line-height:1.2}
.item p{font-size:7px;line-height:1.35;color:var(--ink-soft)}
.item--center{text-align:center;width:250px}
.item--right{text-align:right;width:260px}
.item--left{width:260px}
.num-white{position:absolute;font-weight:700;font-size:19px;color:#fff;line-height:1}

.table-title{position:absolute;font-weight:700;font-size:16px;color:var(--red)}
.table-sub{position:absolute;font-size:7px;line-height:1.3;color:var(--red)}
.table-sub b{font-weight:700}
.grid{position:absolute;width:430px;border-collapse:collapse;table-layout:fixed}
.grid th{background:var(--red);color:#fff;font-size:6.5px;font-weight:400;height:14px;text-align:left;padding-left:11px}
.grid th.c4{padding-left:22px}
.grid td{border-bottom:1px solid #6e6e6e}
.grid .c1,.grid .c3{width:104px}
.grid .c2{width:131px}
.grid .c4{width:91px}
.grid td.c1,.grid td.c3{background:var(--cell-light)}
.grid td.c2{background:var(--cell-mid)}
.grid td.c4{background:var(--cell-dark)}

.chart-label{position:absolute;font-size:7px;color:var(--ink)}
.chart-year{position:absolute;font-size:7px;font-weight:700;color:var(--red)}
</style>
</head>
<body>

<!-- Cover -->
<section class="page page--white" style="left:76px;top:80px">
  <svg class="backdrop" viewBox="0 0 506 710">
    <defs>
      <linearGradient id="coverPhoto" x1="0" y1="0" x2="1" y2="1">
        <stop offset="0" stop-color="#5a5552"/><stop offset=".5" stop-color="#9c9794"/><stop offset="1" stop-color="#6c6866"/>
      </linearGradient>
    </defs>
    <polygon points="0,0 506,0 506,457 0,174" fill="url(#coverPhoto)" role="img" aria-label="Black and white photo of a Victorian house behind bare trees"/>
    <polygon points="330,359 506,250 506,457" fill="#d8262b" opacity=".85"/>
    <polygon points="0,174 506,457 506,557 0,269" fill="var(--red)"/>
    <polygon points="0,269 126,341 0,409" fill="#5b5b5b"/>
  </svg>
  <div class="brand" style="left:38px;top:437px;font-size:22px">
    <span class="brand-dot" style="width:26px;height:26px"></span>
    <span class="brand-name">Bureau<br>Ostrelle</span>
  </div>
  <h1 class="abs" style="left:38px;top:508px;font-family:'Nunito Sans',sans-serif;font-weight:800;font-size:28px;line-height:1.05;color:var(--ink)">Templates Word Bureau<br>Ostrelle</h1>
  <div class="rule" style="left:38px;top:566px;width:145px;height:3px;background:var(--ink)"></div>
  <p class="abs" style="left:38px;top:585px;width:350px;font-size:7.6px;line-height:1.55;color:var(--ink)">I Would Like to Meet In Person and discuss dummy text but gives an idea of what real text will look like in the final product ipsam odio blandit eget nec lectus. Aliquam mi amcorper sem.Lorem ipsum dolor sit amet, wisi non lacus neque augue. this opportunity Forher. You can contact me 20455123780 or E-mail me at hello@ostrelle-mail.com</p>
</section>

<!-- Notes & tables -->
<section class="page page--white" style="left:625px;top:80px">
  <div class="brand" style="left:366px;top:39px;font-size:15px">
    <span class="brand-dot" style="width:18px;height:18px"></span>
    <span class="brand-name">Bureau<br>Ostrelle</span>
  </div>
  <h2 class="abs" style="left:38px;top:68px;font-size:24px;font-weight:700;color:var(--red)">Notes</h2>
  <div class="rule" style="left:38px;top:96px;width:110px"></div>
  <p class="abs" style="left:38px;top:112px;width:406px;font-size:9.2px;line-height:1.55;font-style:italic;font-weight:700;color:#6a6a6a;text-align:justify">I Would Like to Meet In Person and discuss orem ipsum is a name for a common type of placeholder text. simply copy filler or dummy text this is that serves to fill a space without actually saying anything this opportunity Forher. You can contact me at + 20455123780 or E-mail me at hello@ostrelle-mail.</p>
  <div class="table-title" style="left:38px;top:220px">Table Your Company Text</div>
  <div class="table-sub" style="left:38px;top:242px"><b>More chices and visual trends</b><br>Design inspiration for presentation</div>
  <table class="grid" style="left:38px;top:274px">
    <tr><th class="c1">Visualt trends</th><th class="c2">TextbTitle</th><th class="c3">TextbTitle</th><th class="c4">Text</th></tr>
    <tr style="height:18px"><td class="c1"></td><td class="c2"></td><td class="c3"></td><td class="c4"></td></tr>
    <tr style="height:18px"><td class="c1"></td><td class="c2"></td><td class="c3"></td><td class="c4"></td></tr>
    <tr style="height:18px"><td class="c1"></td><td class="c2"></td><td class="c3"></td><td class="c4"></td></tr>
    <tr style="height:18px"><td class="c1"></td><td class="c2"></td><td class="c3"></td><td class="c4"></td></tr>
    <tr style="height:18px"><td class="c1"></td><td class="c2"></td><td class="c3"></td><td class="c4"></td></tr>
    <tr style="height:18px"><td class="c1"></td><td class="c2"></td><td class="c3"></td><td class="c4"></td></tr>
  </table>
  <table class="grid" style="left:38px;top:443px">
    <tr><th class="c1">Visualt trends</th><th class="c2">TextbTitle</th><th class="c3">TextbTitle</th><th class="c4">Text</th></tr>
    <tr style="height:20.5px"><td class="c1"></td><td class="c2"></td><td class="c3"></td><td class="c4"></td></tr>
    <tr style="height:20.5px"><td class="c1"></td><td class="c2"></td><td class="c3"></td><td class="c4"></td></tr>
    <tr style="height:20.5px"><td class="c1"></td><td class="c2"></td><td class="c3"></td><td class="c4"></td></tr>
    <tr style="height:20.5px"><td class="c1"></td><td class="c2"></td><td class="c3"></td><td class="c4"></td></tr>
    <tr style="height:20.5px"><td class="c1"></td><td class="c2"></td><td class="c3"></td><td class="c4"></td></tr>
    <tr style="height:20.5px"><td class="c1"></td><td class="c2"></td><td class="c3"></td><td class="c4"></td></tr>
    <tr style="height:20.5px"><td class="c1"></td><td class="c2"></td><td class="c3"></td><td class="c4"></td></tr>
    <tr style="height:20.5px"><td class="c1"></td><td class="c2"></td><td class="c3"></td><td class="c4"></td></tr>
  </table>
</section>

<!-- Market solutions -->
<section class="page" style="left:76px;top:855px">
  <svg class="backdrop" viewBox="0 0 506 710">
    <defs>
      <radialGradient id="photoRedA" cx=".6" cy=".5" r=".7">
        <stop offset="0" stop-color="var(--photo-red-a)"/><stop offset="1" stop-color="var(--photo-red-b)"/>
      </radialGradient>
    </defs>
    <circle cx="-23" cy="323" r="235" fill="var(--red-deep)"/>
    <circle cx="-23" cy="323" r="186" fill="url(#photoRedA)" role="img" aria-label="Red-tinted photo of a brick building facade"/>
  </svg>
  <div class="brand" style="left:37px;top:24px;font-size:22px">
    <span class="brand-dot" style="width:26px;height:26px"></span>
    <span class="brand-name">Bureau<br>Ostrelle</span>
  </div>
  <div class="section-title" style="left:252px;top:61px">Market Solutions.</div>
  <div class="rule" style="left:271px;top:86px;width:131px"></div>

  <div class="badge" style="left:324px;top:110px">01.</div>
  <div class="item item--center abs" style="left:214px;top:148px"><h4>Bureau Ostrelle</h4><p>Lorem ipsum is a name for a common type of placehold text.<br>simply copy filler or dummy text this is that serves.</p></div>
  <div class="badge" style="left:324px;top:213px">01.</div>
  <div class="item item--center abs" style="left:214px;top:251px"><h4>Bureau Ostrelle</h4><p>Lorem ipsum is a name for a common type of placehold text.<br>simply copy filler or dummy text this is that serves.</p></div>
  <div class="badge" style="left:324px;top:315px">01.</div>
  <div class="item item--center abs" style="left:214px;top:353px"><h4>Bureau Ostrelle</h4><p>Lorem ipsum is a name for a common type of placehold text.<br>simply copy filler or dummy text this is that serves.</p></div>
  <div class="badge" style="left:324px;top:416px">01.</div>
  <div class="item item--center abs" style="left:219px;top:454px"><h4>Bureau Ostrelle</h4><p>Lorem ipsum is a name for a common type of placehold text.<br>simply copy filler or dummy text this is that serves.</p></div>
  <div class="badge" style="left:324px;top:518px">01.</div>
  <div class="item item--center abs" style="left:214px;top:556px"><h4>Bureau Ostrelle</h4><p>Lorem ipsum is a name for a common type of placehold text.<br>simply copy filler or dummy text this is that serves.</p></div>
</section>

<!-- Solutions & problems diamonds -->
<section class="page" style="left:625px;top:853px">
  <svg class="backdrop" viewBox="0 0 506 710">
    <defs>
      <linearGradient id="photoRedB" x1="0" y1="0" x2="1" y2="1">
        <stop offset="0" stop-color="var(--photo-red-b)"/><stop offset=".5" stop-color="var(--photo-red-a)"/><stop offset="1" stop-color="var(--photo-red-b)"/>
      </linearGradient>
    </defs>
    <rect x="-90" y="75" width="246" height="246" rx="24" transform="rotate(45 33 198)" fill="var(--red-deep)"/>
    <rect x="-63" y="102" width="192" height="192" rx="18" transform="rotate(45 33 198)" fill="url(#photoRedB)" role="img" aria-label="Red-tinted photo of people outside a brick building"/>
    <rect x="341" y="411" width="246" height="246" rx="24" transform="rotate(45 464 534)" fill="var(--red-deep)"/>
    <rect x="368" y="438" width="192" height="192" rx="18" transform="rotate(45 464 534)" fill="url(#photoRedB)" role="img" aria-label="Red-tinted photo of a bicycle by a brick wall"/>
  </svg>
  <div class="section-title" style="left:122px;top:39px">Solutions.</div>
  <div class="rule" style="left:122px;top:64px;width:131px"></div>
  <div class="brand" style="left:313px;top:29px;font-size:22px">
    <span class="brand-dot" style="width:26px;height:26px"></span>
    <span class="brand-name">Bureau<br>Ostrelle</span>
  </div>

  <div class="badge" style="left:98px;top:83px">01.</div>
  <div class="item item--left abs" style="left:143px;top:79px"><h4>Bureau Ostrelle</h4><p>Lorem ipsum is a name for a common type of placehold er text.<br>simply copy filler or dummy text this is that serves.</p></div>
  <div class="badge" style="left:139px;top:121px">02.</div>
  <div class="item item--left abs" style="left:184px;top:118px"><h4>Bureau Ostrelle</h4><p>Lorem ipsum is a name for a common type of placehold er text.<br>simply copy filler or dummy text this is that serves.</p></div>
  <div class="badge" style="left:189px;top:180px">03.</div>
  <div class="item item--left abs" style="left:233px;top:178px"><h4>Bureau Ostrelle</h4><p>Lorem ipsum is a name for a common type of placehold er text.<br>simply copy filler or dummy text this is that serves.</p></div>
  <div class="badge" style="left:144px;top:238px">04.</div>
  <div class="item item--left abs" style="left:187px;top:239px"><h4>Bureau Ostrelle</h4><p>Lorem ipsum is a name for a common type of placehold er text.<br>simply copy filler or dummy text this is that serves.</p></div>
  <div class="badge" style="left:89px;top:296px">05.</div>
  <div class="item item--left abs" style="left:131px;top:297px"><h4>Bureau Ostrelle</h4><p>Lorem ipsum is a name for a common type of placehold er text.<br>simply copy filler or dummy text this is that serves.</p></div>

  <div class="section-title" style="right:128px;top:369px">Problame</div>
  <div class="rule" style="left:249px;top:396px;width:130px"></div>

  <div class="badge" style="left:355px;top:416px">01.</div>
  <div class="item item--right abs" style="right:157px;top:413px"><h4>Bureau Ostrelle</h4><p>Lorem ipsum is a name for a common type of placehold er<br>text. simply copy filler or dummy text this is that serves.</p></div>
  <div class="badge" style="left:307px;top:464px">02.</div>
  <div class="item item--right abs" style="right:205px;top:463px"><h4>Bureau Ostrelle</h4><p>Lorem ipsum is a name for a common type of placehold er<br>text. simply copy filler or dummy text this is that serves.</p></div>
  <div class="badge" style="left:271px;top:513px">03.</div>
  <div class="item item--right abs" style="right:241px;top:512px"><h4>Bureau Ostrelle</h4><p>Lorem ipsum is a name for a common type of placehold er<br>text. simply copy filler or dummy text this is that serves.</p></div>
  <div class="badge" style="left:305px;top:569px">04.</div>
  <div class="item item--right abs" style="right:207px;top:568px"><h4>Bureau Ostrelle</h4><p>Lorem ipsum is a name for a common type of placehold er<br>text. simply copy filler or dummy text this is that serves.</p></div>
  <div class="badge" style="left:353px;top:621px">05.</div>
  <div class="item item--right abs" style="right:159px;top:622px"><h4>Bureau Ostrelle</h4><p>Lorem ipsum is a name for a common type of placehold er<br>text. simply copy filler or dummy text this is that serves.</p></div>
</section>

<!-- Problems & solutions circles -->
<section class="page" style="left:76px;top:1618px">
  <svg class="backdrop" viewBox="0 0 506 710">
    <defs>
      <radialGradient id="photoRedC" cx=".5" cy=".5" r=".7">
        <stop offset="0" stop-color="var(--photo-red-a)"/><stop offset="1" stop-color="var(--photo-red-b)"/>
      </radialGradient>
    </defs>
    <circle cx="1" cy="229" r="167" fill="var(--red-deep)"/>
    <circle cx="-6" cy="229" r="132" fill="url(#photoRedC)" role="img" aria-label="Red-tinted photo of people by a brick building"/>
    <circle cx="497" cy="533" r="166" fill="var(--red-deep)"/>
    <circle cx="504" cy="533" r="131" fill="url(#photoRedC)" role="img" aria-label="Red-tinted photo of a bicycle by a brick wall"/>
  </svg>
  <div class="section-title" style="left:122px;top:72px">Problems.</div>
  <div class="rule" style="left:122px;top:98px;width:131px"></div>
  <div class="brand" style="left:297px;top:52px;font-size:22px">
    <span class="brand-dot" style="width:26px;height:26px"></span>
    <span class="brand-name">Bureau<br>Ostrelle</span>
  </div>

  <div class="num-white" style="left:108px;top:120px">01.</div>
  <div class="item item--left abs" style="left:160px;top:122px"><h4>Bureau Ostrelle</h4><p>Lorem ipsum is a name for a common type of placehold er text.<br>simply copy filler or dummy text this is that serves.</p></div>
  <div class="num-white" style="left:134px;top:167px">02.</div>
  <div class="item item--left abs" style="left:176px;top:169px"><h4>Bureau Ostrelle</h4><p>Lorem ipsum is a name for a common type of placehold er text.<br>simply copy filler or dummy text this is that serves.</p></div>
  <div class="num-white" style="left:143px;top:213px">03.</div>
  <div class="item item--left abs" style="left:179px;top:215px"><h4>Bureau Ostrelle</h4><p>Lorem ipsum is a name for a common type of placehold er text.<br>simply copy filler or dummy text this is that serves.</p></div>
  <div class="num-white" style="left:134px;top:259px">04.</div>
  <div class="item item--left abs" style="left:176px;top:261px"><h4>Bureau Ostrelle</h4><p>Lorem ipsum is a name for a common type of placehold er text.<br>simply copy filler or dummy text this is that serves.</p></div>
  <div class="num-white" style="left:109px;top:306px">05.</div>
  <div class="item item--left abs" style="left:156px;top:309px"><h4>Bureau Ostrelle</h4><p>Lorem ipsum is a name for a common type of placehold er text.<br>simply copy filler or dummy text this is that serves.</p></div>

  <div class="section-title" style="right:128px;top:364px">Solutions.</div>
  <div class="rule" style="left:248px;top:389px;width:130px"></div>

  <div class="num-white" style="left:382px;top:409px">01.</div>
  <div class="item item--right abs" style="right:157px;top:410px"><h4>Bureau Ostrelle</h4><p>Lorem ipsum is a name for a common type of placehold er<br>text. simply copy filler or dummy text this is that serves.</p></div>
  <div class="num-white" style="left:354px;top:460px">02.</div>
  <div class="item item--right abs" style="right:178px;top:459px"><h4>Bureau Ostrelle</h4><p>Lorem ipsum is a name for a common type of placehold er<br>text. simply copy filler or dummy text this is that serves.</p></div>
  <div class="num-white" style="left:339px;top:508px">03.</div>
  <div class="item item--right abs" style="right:184px;top:508px"><h4>Bureau Ostrelle</h4><p>Lorem ipsum is a name for a common type of placehold er<br>text. simply copy filler or dummy text this is that serves.</p></div>
  <div class="num-white" style="left:341px;top:560px">04.</div>
  <div class="item item--right abs" style="right:182px;top:560px"><h4>Bureau Ostrelle</h4><p>Lorem ipsum is a name for a common type of placehold er<br>text. simply copy filler or dummy text this is that serves.</p></div>
  <div class="num-white" style="left:360px;top:610px">05.</div>
  <div class="item item--right abs" style="right:162px;top:611px"><h4>Bureau Ostrelle</h4><p>Lorem ipsum is a name for a common type of placehold er<br>text. simply copy filler or dummy text this is that serves.</p></div>
</section>

<!-- Tables & market growth -->
<section class="page" style="left:625px;top:1618px">
  <div class="brand" style="left:38px;top:37px;font-size:22px">
    <span class="brand-dot" style="width:26px;height:26px"></span>
    <span class="brand-name">Bureau<br>Ostrelle</span>
  </div>
  <div class="table-title" style="left:38px;top:96px">Table Your Company Text</div>
  <div class="table-sub" style="left:38px;top:117px"><b>More chices and visual trends</b><br>Design inspiration for presentation</div>
  <table class="grid" style="left:38px;top:149px">
    <tr><th class="c1">Visualt trends</th><th class="c2">TextbTitle</th><th class="c3">TextbTitle</th><th class="c4">Text</th></tr>
    <tr style="height:19px"><td class="c1"></td><td class="c2"></td><td class="c3"></td><td class="c4"></td></tr>
    <tr style="height:19px"><td class="c1"></td><td class="c2"></td><td class="c3"></td><td class="c4"></td></tr>
    <tr style="height:19px"><td class="c1"></td><td class="c2"></td><td class="c3"></td><td class="c4"></td></tr>
    <tr style="height:19px"><td class="c1"></td><td class="c2"></td><td class="c3"></td><td class="c4"></td></tr>
  </table>
  <table class="grid" style="left:38px;top:242px">
    <tr><th class="c1">Visualt trends</th><th class="c2">TextbTitle</th><th class="c3">TextbTitle</th><th class="c4">Text</th></tr>
    <tr style="height:18px"><td class="c1"></td><td class="c2"></td><td class="c3"></td><td class="c4"></td></tr>
    <tr style="height:18px"><td class="c1"></td><td class="c2"></td><td class="c3"></td><td class="c4"></td></tr>
    <tr style="height:18px"><td class="c1"></td><td class="c2"></td><td class="c3"></td><td class="c4"></td></tr>
    <tr style="height:18px"><td class="c1"></td><td class="c2"></td><td class="c3"></td><td class="c4"></td></tr>
  </table>

  <h3 class="abs" style="left:0;width:516px;text-align:center;top:381px;font-size:20px;font-weight:700;color:#333">Market Grwoth</h3>
  <div class="abs" style="left:0;width:506px;text-align:center;top:423px;font-size:13px;font-weight:700;line-height:1;color:#333">Write Your Compsny<br>Headline Here</div>
  <p class="abs" style="left:94px;width:322px;text-align:center;top:459px;font-size:6.8px;line-height:1.4;color:var(--ink)">I Would Like to Meet In Person and discuss dummy text but gives an idea of what real text will look like in the final produ ct ipsam odio blandit eget nec lectus. Aliquam mi amcorper sem.Lorem ipsum dolor sit amet, wisi non lacus neque augue. this opportunity Forher. You can contact me 20455123780 or E-mail me at hello@ostrelle-mail.com</p>

  <svg class="abs" style="left:0;top:0" width="506" height="710" viewBox="0 0 506 710" role="img" aria-label="Bar chart of market growth 2016 to 2019">
    <g stroke="#9a9a9a" stroke-width=".8">
      <line x1="117" y1="522" x2="371" y2="522"/>
      <line x1="117" y1="565" x2="371" y2="565"/>
      <line x1="117" y1="608" x2="371" y2="608"/>
      <line x1="117" y1="651" x2="371" y2="651"/>
    </g>
    <g fill="#e31e24">
      <rect x="158" y="608" width="16" height="43"/>
      <rect x="213" y="565" width="16" height="86"/>
      <rect x="267" y="522" width="16" height="129"/>
      <rect x="322" y="565" width="16" height="86"/>
    </g>
  </svg>
  <div class="chart-label" style="left:105px;top:518px">30</div>
  <div class="chart-label" style="left:105px;top:561px">30</div>
  <div class="chart-label" style="left:105px;top:604px">30</div>
  <div class="chart-label" style="left:105px;top:647px">30</div>
  <div class="chart-label" style="left:152px;top:599px">Labal A</div>
  <div class="chart-label" style="left:207px;top:556px">Labal A</div>
  <div class="chart-label" style="left:261px;top:513px">Labal A</div>
  <div class="chart-label" style="left:316px;top:556px">Labal A</div>
  <div class="chart-year" style="left:156px;top:655px">2016</div>
  <div class="chart-year" style="left:211px;top:655px">2017</div>
  <div class="chart-year" style="left:265px;top:655px">2018</div>
  <div class="chart-year" style="left:320px;top:655px">2019</div>
</section>

</body>
</html>
```